We need an eye catching logo design and Business Card that portrays our business, which is the cleaning and protecting of stainless steel with an organic non chemical product. This can be separate to the company name or can incorporate it. Maybe even just the company name itself. Company Name is Gleamwise Gleamwise.
Ideal for products exposed to weather elements, ie: balustrading, enclosures, BBQs, we also supply the product so you can do it yourself (DIY).
In addition we would want to include on this card:
1. My Name (Paul Dremmick)
2. Mobile No. (TBA Later)
3. Email address (TBA Later)
4. Web address (TBA Later)
Updates

Please note that we also need suggestions on a logo, as this we do not have this either.

Please note we have update our brief to be more specific.

Thank You.

Paul

Reason: Awaiting for a couple of revised submissions from feedback given.

Target Market(s)

Purchasing officers and government people.

Industry/Entity Type

Steel

Colors

Designer to choose colors to be used in the design.

Requirements
Must have
• 1. Name (Paul Dremmick)
2. Mobile No. (TBA Later)
Should not have
• Should not be to busy looking

```html
<!DOCTYPE html>
<html lang="en">
<head>
<meta charset="utf-8">
<title>Gleamwise Gleamwise – Business Card</title>
<link href="https://fonts.googleapis.com/css2?family=Exo+2:wght@300;400;800&display=swap" rel="stylesheet">
<style>
  :root {
    --backdrop-top: #8f8f8f;
    --backdrop-bottom: #e6e6e6;
    --card-dark: #48494b;
    --text-light: #c9c9c9;
    --text-soft: #a9a9a9;
    --metal-light: #e9e9e9;
    --metal-mid: #bdbdbd;
    --metal-dark: #8a8a8a;
    --logo-ink: #1c1c1c;
  }
  * { margin: 0; padding: 0; box-sizing: border-box; }
  html, body {
    width: 1200px; height: 823px; overflow: hidden;
  }
  body {
    background: linear-gradient(180deg, var(--backdrop-top) 0%, var(--backdrop-bottom) 100%);
    font-family: "Exo 2", sans-serif;
    position: relative;
  }
  .card {
    position: absolute;
    top: 268px;
    width: 500px;
    height: 286px;
    box-shadow: 0 12px 28px rgba(0,0,0,0.28);
    overflow: hidden;
  }
  .card-back { left: 70px; background: var(--card-dark); }
  .card-front { left: 630px; }

  .metal {
    position: absolute;
    background:
      radial-gradient(circle at 50% 50%, rgba(255,255,255,0.35) 0%, rgba(255,255,255,0) 45%),
      conic-gradient(from 0deg at 50% 50%,
        var(--metal-light), var(--metal-mid), var(--metal-dark), var(--metal-mid),
        var(--metal-light), var(--metal-mid), var(--metal-dark), var(--metal-mid), var(--metal-light));
  }
  .metal-strip { top: 0; right: 0; width: 66px; height: 100%; }
  .metal-face { inset: 0; }

  .contact {
    position: absolute;
    left: 22px;
    top: 128px;
    color: var(--text-light);
    font-weight: 300;
  }
  .contact-name {
    font-size: 16px; font-weight: 400; letter-spacing: 0.5px;
    margin-left: 10px;
  }
  .contact-role {
    font-size: 11px; color: var(--text-soft);
    margin-left: 12px; margin-bottom: 8px;
  }
  .contact-row {
    display: flex; align-items: center; gap: 7px;
    font-size: 11.5px; line-height: 17px;
  }
  .contact-row svg { width: 10px; height: 10px; fill: var(--text-soft); flex: none; }
  .contact-gap { height: 22px; }
  .inline-gap { margin-left: 22px; display: inline-flex; align-items: center; gap: 6px; }

  .brand-name {
    position: absolute;
    left: 0; right: 0; top: 50%;
    transform: translateY(-50%);
    text-align: center;
    font-size: 52px;
    font-weight: 800;
    letter-spacing: 1px;
    color: var(--logo-ink);
  }
</style>
</head>
<body>

  <section class="card card-back" aria-label="Business card back">
    <div class="metal metal-strip" role="img" aria-label="Brushed stainless steel texture"></div>
    <div class="contact">
      <p class="contact-name">PAUL DREMMICK</p>
      <p class="contact-role">Designation</p>
      <p class="contact-row">
        <svg viewBox="0 0 10 10"><rect x="2.5" y="0" width="5" height="10" rx="1"/></svg>
        +012 345 6780
      </p>
      <p class="contact-row">
        <svg viewBox="0 0 10 10"><rect x="0" y="2" width="10" height="6.5" rx="0.8"/></svg>
        p.dremmick@gleamwisegleamwise.com
      </p>
      <div class="contact-gap"></div>
      <p class="contact-row">
        <svg viewBox="0 0 10 10"><path d="M5 0a3.5 3.5 0 0 0-3.5 3.5C1.5 6 5 10 5 10s3.5-4 3.5-6.5A3.5 3.5 0 0 0 5 0zm0 5a1.4 1.4 0 1 1 0-2.8A1.4 1.4 0 0 1 5 5z"/></svg>
        01 Avenue, Suite No. 123, Your City, Country
      </p>
      <p class="contact-row">
        <svg viewBox="0 0 10 10"><path d="M2 0.5l2 2-1 1.3a6 6 0 0 0 3.2 3.2l1.3-1 2 2-1.3 1.5C4.5 9.3 0.7 5.5 0.5 1.8z"/></svg>
        +012 345 6789
        <span class="inline-gap">
          <svg viewBox="0 0 10 10"><rect x="0" y="4" width="10" height="6"/><rect x="2" y="0" width="5" height="4"/></svg>
          +012 345 6780
        </span>
      </p>
      <p class="contact-row">
        <svg viewBox="0 0 10 10"><circle cx="5" cy="5" r="4.5"/></svg>
        www.GleamwiseGleamwise.com
      </p>
    </div>
  </section>

  <section class="card card-front" aria-label="Business card front">
    <div class="metal metal-face" role="img" aria-label="Brushed stainless steel texture"></div>
    <p class="brand-name">GLEAMWISE</p>
  </section>

</body>
</html>
```